Dog breeder design card

A card for our dog showing/breeding and companion puppy buyers.
Updates

Reason: The photo's I provided were not seen by designers because of a glitch or error, so I will need to start them over again in the designs submitted to me. I uploaded and emailed the photo's last night.

Thank you all so much for your lovely designs, I like wquite a few of them. I provided images in my original brief, but these apparently did not become available for you to see. I have emailed my images now, so hopefully you may be able to incorporate them into your designs.

Thank you so much for your time,
kind regards,
Beatrice

I have attached the photo’s that can hopefully be incorporated onto my business card. I don’t mind if the whole images aren’t used, but maybe a soft focus look around the adult dog and in a corner of the card maybe....if that’s possible.

Contact Information for Business Card

Corvanel Bullmastiffs, adored by Gerald and Beatrice Lindqvist.
Tallowmere VIC
0478 552961

Requirements
Nice to have
• Soft focus look to the outline of adult dogs head incorporated into perhaps a corner of the card. Soft focus outline around pups perhaps.
I do really love hot pink and/or purple text if possible.
"Corvanel Bullmastiffs" to be incorporated on the front of card, our details on reverse.
Would prefer a glossy finish rather than matt.

```html
<!DOCTYPE html>
<html lang="en">
<head>
<meta charset="utf-8">
<title>Corvanel Bullmastiff – Business Card</title>
<link href="https://fonts.googleapis.com/css2?family=Questrial&display=swap" rel="stylesheet">
<style>
  :root {
    --page: #e9ecef;
    --card-blue: #0b84c6;
    --card-glow: #4aa6d6;
    --ink-white: #ffffff;
    --mark-fill: #d6dbe0;
    --rule-silver: #dfe6ea;
  }
  * { box-sizing: border-box; margin: 0; padding: 0; }
  html, body {
    width: 1200px;
    height: 646px;
    overflow: hidden;
    background: var(--page);
    font-family: "Questrial", "Century Gothic", sans-serif;
    color: var(--ink-white);
  }
  .sheet {
    width: 1200px;
    height: 646px;
    display: flex;
    align-items: center;
    justify-content: center;
    gap: 60px;
  }
  .card {
    position: relative;
    width: 520px;
    height: 297px;
    border-radius: 3px;
    background: radial-gradient(ellipse at 40% 35%, var(--card-glow) 0%, var(--card-blue) 70%);
    box-shadow: 0 6px 18px rgba(0,0,0,0.18);
    overflow: hidden;
  }

  /* Reverse */
  .card-back .edge-rule {
    position: absolute;
    left: 38px;
    top: 18px;
    width: 4px;
    height: 240px;
    background: var(--rule-silver);
    border-radius: 2px;
  }
  .card-back .mini-mark {
    position: absolute;
    top: 22px;
    left: 50%;
    transform: translateX(-50%);
    display: flex;
    flex-direction: column;
    align-items: center;
    gap: 6px;
  }
  .card-back .mini-square {
    width: 32px;
    height: 32px;
    background: var(--mark-fill);
  }
  .card-back .mini-name {
    font-size: 14px;
    letter-spacing: 0.5px;
    white-space: nowrap;
  }
  .card-back .details {
    position: absolute;
    left: 0;
    right: 0;
    top: 116px;
    text-align: center;
  }
  .details .lead { font-size: 23px; letter-spacing: 0.5px; line-height: 1.2; }
  .details .owners { font-size: 23px; letter-spacing: 0.5px; line-height: 1.2; }
  .details .contact { font-size: 14px; letter-spacing: 0.6px; margin-top: 6px; }

  /* Front */
  .card-front .mark-square {
    position: absolute;
    left: 50%;
    top: 48px;
    transform: translateX(-50%);
    width: 110px;
    height: 110px;
    background: var(--mark-fill);
  }
  .card-front .brand {
    position: absolute;
    left: 0;
    right: 0;
    top: 184px;
    text-align: center;
    font-size: 40px;
    font-weight: 400;
    letter-spacing: 1px;
    line-height: 1;
    white-space: nowrap;
  }
</style>
</head>
<body>
  <main class="sheet">
    <section class="card card-back" aria-label="Card reverse">
      <span class="edge-rule" aria-hidden="true"></span>
      <div class="mini-mark">
        <span class="mini-square" aria-hidden="true"></span>
        <span class="mini-name">Corvanel Bullmastiff</span>
      </div>
      <div class="details">
        <p class="lead">Adored by;</p>
        <p class="owners">Gerald and Beatrice Lindqvist.</p>
        <p class="contact">Tallowmere VIC 0478 552961</p>
      </div>
    </section>

    <section class="card card-front" aria-label="Card front">
      <span class="mark-square" aria-hidden="true"></span>
      <h1 class="brand">Corvanel Bullmastiff</h1>
    </section>
  </main>
</body>
</html>
```